Powepoint Templates From Logo

Hello,

I am looking for a template for PowerPoint presentations for a new company selling LED's. The PowerPoint should keep the look and feel of our newly designed website ( which is still under development ) http://brivoxa.com/development/

I have attached our Logo which should be included in this template.
This PowerPoint will be used towards client during demonstrations and for internal use.

This template should be complete with fonts and colors of the text for both headlines and bullets/normal text.

I guess the easiest way for me to determine what I like is to see some dummy info/text on the submitted designs.

Thanks

Industry/Entity Type

It Company

Requirements
Must have
• Should include our logo

```html
<!DOCTYPE html>
<html lang="en">
<head>
<meta charset="utf-8">
<title>Brivoxa – Presentation Template</title>
<link rel="stylesheet" href="https://fonts.googleapis.com/css2?family=Michroma&family=Carlito:wght@400;700&display=swap">
<style>
  :root {
    --page: #ffffff;
    --slide: #ffffff;
    --slide-border: #c9c9c9;
    --rule: #d6d6d6;
    --band-dark: #2f2f2f;
    --band-mid: #4a4a4a;
    --brand-green: #a8cf1a;
    --subtitle-green: #b3d30f;
    --text: #5a5a5a;
    --text-soft: #666666;
    --panel: #f4f4f4;
    --title-bar-top: #8e8e8e;
    --title-bar-bottom: #d9d9d9;
    --brand-grey: #8a8a8a;
    --white: #ffffff;
  }
  * { box-sizing: border-box; margin: 0; padding: 0; }
  html, body { width: 1200px; height: 555px; overflow: hidden; background: var(--page); }
  body { position: relative; font-family: "Carlito", "Calibri", sans-serif; color: var(--text); }

  .slide {
    position: absolute; top: 65px; width: 574px; height: 430px;
    background: var(--slide); border: 1px solid var(--slide-border);
    box-shadow: 1px 2px 3px rgba(0,0,0,0.25);
  }
  .slide--cover { left: 12px; }
  .slide--content { left: 609px; }

  /* Brand mark */
  .brand { position: absolute; display: flex; align-items: center; gap: 8px; }
  .brand__dot { border-radius: 50%; background: var(--brand-green); }
  .brand__name { font-family: "Carlito", sans-serif; font-weight: 700; color: var(--brand-grey); }
  .slide--cover .brand { left: 28px; top: 26px; }
  .slide--cover .brand__dot { width: 62px; height: 62px; }
  .slide--cover .brand__name { font-size: 40px; }
  .slide--content .brand { right: 12px; bottom: 8px; gap: 5px; }
  .slide--content .brand__dot { width: 24px; height: 24px; }
  .slide--content .brand__name { font-size: 17px; }

  /* Cover */
  .rule { position: absolute; left: 0; right: 0; height: 3px; background: var(--rule); }
  .rule--top { top: 117px; }
  .rule--bottom { top: 331px; }
  .hero-band {
    position: absolute; left: 0; right: 0; top: 134px; height: 184px;
    background: linear-gradient(90deg, var(--band-dark) 0%, var(--band-mid) 70%, var(--band-dark) 100%);
  }
  .hero-band__product {
    position: absolute; left: 330px; top: 10px; width: 200px; height: 164px;
    background: radial-gradient(ellipse at 50% 60%, #d8d8d8 0%, #9a9a9a 25%, rgba(80,80,80,0) 65%);
  }
  .cover-title {
    position: absolute; left: 17px; top: 82px;
    font-family: "Michroma", sans-serif; font-size: 20px; letter-spacing: 1px;
    color: var(--white);
  }
  .cover-subtitle {
    position: absolute; left: 17px; top: 343px;
    font-size: 18px; color: var(--subtitle-green);
  }

  /* Content slide */
  .title-bar {
    position: absolute; left: 10px; top: 9px; width: 551px; height: 66px;
    background: linear-gradient(180deg, var(--title-bar-top), var(--title-bar-bottom));
    box-shadow: 0 2px 3px rgba(0,0,0,0.2);
  }
  .title-bar__text {
    position: absolute; left: 6px; top: 21px;
    font-family: "Michroma", sans-serif; font-size: 19px; letter-spacing: 1px; color: var(--white);
  }
  .content-panel {
    position: absolute; left: 13px; top: 93px; width: 550px; height: 292px;
    background: var(--panel); box-shadow: 1px 2px 3px rgba(0,0,0,0.25);
  }
  .clip { position: absolute; top: -8px; }
  .clip--1 { left: 14px; } .clip--2 { left: 193px; } .clip--3 { left: 327px; } .clip--4 { left: 512px; }

  .bullets { position: absolute; left: 6px; top: 14px; width: 535px; list-style: none; }
  .bullets > li {
    position: relative; padding-left: 20px; font-size: 17px; line-height: 17px; margin-bottom: 9px;
  }
  .bullets > li::before {
    content: ""; position: absolute; left: 0; top: 4px; width: 11px; height: 11px;
    border-radius: 50%; background: var(--brand-green);
  }
  .sub-bullets { list-style: none; margin: 9px 0 0 -20px; padding-left: 46px; }
  .sub-bullets li {
    position: relative; padding-left: 0; font-size: 14px; line-height: 16px; margin-bottom: 9px;
    color: var(--text-soft);
  }
  .sub-bullets li::before {
    content: ""; position: absolute; left: -20px; top: 8px; width: 8px; height: 1px;
    background: var(--brand-green);
  }
</style>
</head>
<body>

  <section class="slide slide--cover">
    <div class="brand"><span class="brand__dot"></span><span class="brand__name">Brivoxa</span></div>
    <div class="rule rule--top"></div>
    <div class="hero-band">
      <div class="hero-band__product" role="img" aria-label="Product photo of two LED spotlight bulbs"></div>
      <h1 class="cover-title">PRESENTATION TITLE</h1>
    </div>
    <div class="rule rule--bottom"></div>
    <p class="cover-subtitle">Presentation subtitle</p>
  </section>

  <section class="slide slide--content">
    <div class="title-bar"><h2 class="title-bar__text">SLIDE TITLE</h2></div>
    <div class="content-panel">
      <svg class="clip clip--1" width="14" height="16" viewBox="0 0 14 16" aria-hidden="true"><rect x="1" y="1" width="4" height="14" rx="2" fill="#555"/><rect x="9" y="1" width="4" height="14" rx="2" fill="#555"/><rect x="0" y="6" width="14" height="3" fill="#888"/></svg>
      <svg class="clip clip--2" width="14" height="16" viewBox="0 0 14 16" aria-hidden="true"><rect x="1" y="1" width="4" height="14" rx="2" fill="#555"/><rect x="9" y="1" width="4" height="14" rx="2" fill="#555"/><rect x="0" y="6" width="14" height="3" fill="#888"/></svg>
      <svg class="clip clip--3" width="14" height="16" viewBox="0 0 14 16" aria-hidden="true"><rect x="1" y="1" width="4" height="14" rx="2" fill="#555"/><rect x="9" y="1" width="4" height="14" rx="2" fill="#555"/><rect x="0" y="6" width="14" height="3" fill="#888"/></svg>
      <svg class="clip clip--4" width="14" height="16" viewBox="0 0 14 16" aria-hidden="true"><rect x="1" y="1" width="4" height="14" rx="2" fill="#555"/><rect x="9" y="1" width="4" height="14" rx="2" fill="#555"/><rect x="0" y="6" width="14" height="3" fill="#888"/></svg>

      <ul class="bullets">
        <li>Lorem ipsum dolor sit amet, consectetur adipiscing elit. In sit amet neque turpis.</li>
        <li>Donec vitae dolor fermentum neque euismod adipiscing. Duis nec lectus felis, ut bibendum risus.
          <ul class="sub-bullets">
            <li>Ut sagittis consequat placerat. Mauris non neque vitae dui auctor pharetra ac ac sapien.</li>
            <li>Suspendisse a tempor quam. Integer eu purus eget nunc semper auctor. Class aptent taciti sociosqu ad litora torquent per conubia nostra, per inceptos himenaeos.</li>
            <li>Nam tincidunt magna at lacus semper at lacinia dui feugiat.</li>
          </ul>
        </li>
        <li>Maecenas a nisl at nulla aliquam feugiat nec eu lectus. Etiam nec euismod dui. Proin eu laoreet lacus.</li>
      </ul>
    </div>
    <div class="brand"><span class="brand__dot"></span><span class="brand__name">Brivoxa</span></div>
  </section>

</body>
</html>
```